Recruitment Agency in Texas, needs a stand out header letter

Our colours are red and grey and can be found on our website
just my logo will be sufficient and address...

Target Market(s)

Engineering Manufacturing

Colors
0094D4
00A9DD
6FCCEA
C7EBF8
E9F6FB
EB3D1F
EC4F4E
F09395
F8D3D4
FCEDEE

Requirements
Must have
• use colors red and grey
Should not have
• Please use same colors and font as my logo. My website is kelbrantstaffing.net

```html
<!DOCTYPE html>
<html lang="en">
<head>
<meta charset="utf-8">
<title>Kelbrant Staffing Letterhead</title>
<link rel="stylesheet" href="https://fonts.googleapis.com/css2?family=Montserrat:ital,wght@0,400;0,600;0,700;1,400&display=swap">
<style>
  :root {
    --red: #ec1c24;
    --red-muted: #b5323b;
    --wine: #7a4048;
    --grey: #6d6e71;
    --ink: #3d3d3f;
    --paper: #ffffff;
    --backdrop: #ecebe8;
    --band: linear-gradient(90deg, var(--grey) 0%, var(--grey) 35%, var(--wine) 70%, var(--red-muted) 88%, var(--red) 100%);
  }
  * { box-sizing: border-box; margin: 0; padding: 0; }
  html, body {
    width: 1200px; height: 1200px; overflow: hidden;
    background: var(--backdrop);
    font-family: "Montserrat", sans-serif;
    color: var(--ink);
  }
  .letterhead {
    position: absolute; left: 160px; top: 30px;
    width: 880px; height: 1140px;
    background: var(--paper);
    box-shadow: 0 6px 18px rgba(0,0,0,0.12);
  }
  .brand-name {
    position: absolute; left: 62px; top: 50px;
    font-weight: 700; font-size: 32px; letter-spacing: -0.6px;
    color: var(--red);
  }
  .web-band {
    position: absolute; right: 0; top: 50px;
    width: 296px; height: 37px;
    background: var(--band);
  }
  .web-band .web-icon { position: absolute; left: 14px; top: 9px; width: 19px; height: 19px; }
  .web-band .web-text {
    position: absolute; left: 50px; top: 10px;
    font-size: 12.5px; font-weight: 600; color: #fff;
  }
  .letter-body { position: absolute; left: 182px; top: 0; width: 540px; }
  .letter-date { position: absolute; top: 240px; font-weight: 700; font-size: 16px; }
  .recipient { position: absolute; top: 302px; font-size: 16px; line-height: 22px; }
  .recipient .name { font-weight: 700; }
  .recipient .role { font-style: italic; }
  .body-copy {
    position: absolute; top: 410px; width: 540px;
    font-size: 16px; line-height: 24px;
  }
  .body-copy p { margin-bottom: 20px; }
  .sign-off { position: absolute; top: 826px; font-size: 16px; }
  .signature {
    position: absolute; left: -26px; top: 856px;
    width: 146px; height: 40px;
    background: #f4f4f5; border-radius: 20px;
  }
  .signer { position: absolute; top: 900px; font-weight: 700; font-size: 16px; }
  .footer-band {
    position: absolute; left: 0; bottom: 0;
    width: 880px; height: 113px;
    background: var(--band);
  }
  .contact {
    position: absolute; top: 26px; transform: translateX(-50%);
    text-align: center; color: #fff; font-size: 11px; line-height: 14px;
    white-space: nowrap;
  }
  .contact .icon { display: block; margin: 0 auto 9px; width: 24px; height: 24px; }
  .contact strong { font-weight: 700; }
</style>
</head>
<body>
  <main class="letterhead">
    <div class="brand-name">KelbrantStaffing</div>

    <div class="web-band">
      <svg class="web-icon" viewBox="0 0 24 24" aria-hidden="true">
        <circle cx="12" cy="12" r="10.5" fill="none" stroke="#fff" stroke-width="1.6"/>
        <ellipse cx="12" cy="12" rx="4.5" ry="10.5" fill="none" stroke="#fff" stroke-width="1.4"/>
        <line x1="1.5" y1="12" x2="22.5" y2="12" stroke="#fff" stroke-width="1.4"/>
        <line x1="3.5" y1="6.5" x2="20.5" y2="6.5" stroke="#fff" stroke-width="1.2"/>
        <line x1="3.5" y1="17.5" x2="20.5" y2="17.5" stroke="#fff" stroke-width="1.2"/>
      </svg>
      <span class="web-text">www.kelbrantstaffing.net</span>
    </div>

    <section class="letter-body">
      <p class="letter-date">Date, 01 April 2021</p>
      <div class="recipient">
        <p>To:</p>
        <p class="name">Daniel Hart</p>
        <p class="role">Chief Officer</p>
      </div>
      <div class="body-copy">
        <p>Lorem ipsum dolor sit amet, consectetur adipiscing elit. Duis auctor sem vel metus interdum porta. Duis consequat bibendum felis eget cursus. Nulla eget purus vehicula ipsum finibus egestas. Nullam ligula ipsum, mollis sed gravida vitae, maximus eu dolor. Morbi luctus sem a congue consectetur.</p>
        <p>Orci varius natoque penatibus et magnis dis parturient montes, nascetur ridiculus mus. Vestibulum congue eros auctor, ullamcorper libero blandit, tempor tellus. Proin vitae tellus et nunc fringilla lacinia. Sed augue erat, facilisis laoreet velit a, convallis mattis nunc. Nunc sagittis ligula vitae sollicitudin sollicitudin.</p>
        <p>Nulla facilisi. Nulla quis odio vitae purus aliquam fermentum ut nec diam. Fusce sed velit ultrices, aliquam augue ut, sollicitudin orci.</p>
      </div>
      <p class="sign-off">Kind Regards</p>
      <div class="signature" role="img" aria-label="Handwritten signature of the sender"></div>
      <p class="signer">Daniel Hart</p>
    </section>

    <footer class="footer-band">
      <div class="contact" style="left:172px">
        <svg class="icon" viewBox="0 0 24 24" aria-hidden="true">
          <circle cx="12" cy="12" r="12" fill="var(--red)"/>
          <path d="M12 5a4.5 4.5 0 0 0-4.5 4.5c0 3.4 4.5 8.5 4.5 8.5s4.5-5.1 4.5-8.5A4.5 4.5 0 0 0 12 5z" fill="#fff"/>
          <circle cx="12" cy="9.5" r="1.7" fill="var(--red)"/>
        </svg>
        <strong>Houston Office</strong><br>48 Lakeview Court Houston
      </div>

      <div class="contact" style="left:370px">
        <svg class="icon" viewBox="0 0 24 24" aria-hidden="true">
          <circle cx="12" cy="12" r="12" fill="var(--red)"/>
          <path d="M8.2 6.2l2 2.4-1.2 1.6c.8 1.7 2.1 3 3.8 3.8l1.6-1.2 2.4 2-1.2 2.1c-4.6-.3-8.7-4.4-9-9z" fill="#fff"/>
        </svg>
        (+1) 555-014-2290
      </div>

      <div class="contact" style="left:532px">
        <svg class="icon" viewBox="0 0 24 24" aria-hidden="true">
          <circle cx="12" cy="12" r="12" fill="var(--red)"/>
          <rect x="7" y="9" width="10" height="9" rx="1" fill="#fff"/>
          <rect x="9" y="6" width="6" height="4" fill="#fff"/>
          <rect x="9" y="12" width="6" height="1.3" fill="var(--red)"/>
          <rect x="9" y="14.5" width="6" height="1.3" fill="var(--red)"/>
        </svg>
        555-014-2291
      </div>

      <div class="contact" style="left:713px">
        <svg class="icon" viewBox="0 0 24 24" aria-hidden="true">
          <circle cx="12" cy="12" r="12" fill="var(--red)"/>
          <path d="M6 11.5l12-5-3 12-3.2-3.6-2.3 2 .3-3.2z" fill="#fff"/>
        </svg>
        info@kelbrantstaffing.net
      </div>
    </footer>
  </main>
</body>
</html>
```